Plastic Surgeon Needs a business card desing

I need a plastic surgeon business card, Im young , innovative , not afraid of thinking out of the box, What I dont like is human figures or scalpes as designing the card, because I think they are old fashion, I think my name is my strongest card, so I try to find the desing to be something elegant , simple , slick , stylish , radiant with carimsa!

Target Market(s)

PLastics Surgery Patients and doctors to have my data

Industry/Entity Type

Plastic

Contact Information for Business Card

phone numbers need to be legible , right now i have grey scales so they a not to legible

Font styles to use
Serif
Sans Serif

Requirements
Must have
• Personality, and it has to look like a doctor card, not a buisness man card, that is why i think it should be clean , clear , and legible
Nice to have
• Stylilsh, not to heavy card, in means of colors and logos, i think it should give a sensation of health
• Im not sure to have the logo of the hospital i work
Should not have
• human figures
• Hands
• Surgeons

```html
<!DOCTYPE html>
<html lang="es">
<head>
<meta charset="utf-8">
<title>Dr. Mateo Varela – Tarjeta de presentación</title>
<link href="https://fonts.googleapis.com/css2?family=Dosis:wght@400;500;600&display=swap" rel="stylesheet">
<style>
  :root {
    --navy: #173b57;
    --navy-deep: #0f2c43;
    --white: #ffffff;
    --silver: #d9dee3;
    --accent-blue: #4a8fd0;
    --backdrop: #e6e8ea;
    --stripe-red: #d23a3a;
    --stripe-green: #4caf50;
    --stripe-magenta: #c2185b;
    --stripe-blue: #5b6fc9;
    --stripe-teal: #2e9e6e;
    --stripe-lilac: #b48fc4;
  }
  * { margin: 0; padding: 0; box-sizing: border-box; }
  html, body {
    width: 1200px; height: 930px; overflow: hidden;
    background: var(--backdrop);
    font-family: "Dosis", sans-serif;
  }
  .canvas { position: relative; width: 1200px; height: 930px; }

  .card {
    position: absolute; left: 250px; width: 700px;
    box-shadow: 0 6px 18px rgba(0,0,0,.18);
    overflow: hidden;
  }

  /* Contact side */
  .card--contact { top: 50px; height: 390px; background: var(--navy); color: var(--white); }
  .identity {
    position: absolute; left: 50px; top: 80px; width: 280px; text-align: center;
  }
  .brand-mark {
    display: inline-flex; align-items: center; gap: 10px;
    font-weight: 600; font-size: 26px; letter-spacing: 4px; color: var(--white);
  }
  .brand-mark .dot { width: 12px; height: 12px; border-radius: 50%; background: var(--white); }
  .doctor-name { margin-top: 18px; font-size: 36px; font-weight: 500; letter-spacing: .5px; }
  .specialty { margin-top: 2px; font-size: 14px; font-style: normal; }

  .contact-list {
    position: absolute; left: 410px; top: 88px; list-style: none;
    font-size: 16px; line-height: 27px; letter-spacing: .3px;
  }
  .contact-list li:nth-child(3) { margin-top: 8px; }
  .contact-list li:nth-child(n+3) { padding-left: 8px; }

  .color-rule {
    position: absolute; left: 0; right: 0; top: 290px; height: 4px; display: flex;
  }
  .color-rule span { flex: 1; }
  .color-rule span:nth-child(1) { background: var(--stripe-red); }
  .color-rule span:nth-child(2) { background: var(--stripe-green); }
  .color-rule span:nth-child(3) { background: var(--stripe-magenta); }
  .color-rule span:nth-child(4) { background: var(--stripe-blue); }
  .color-rule span:nth-child(5) { background: var(--stripe-teal); }
  .color-rule span:nth-child(6) { background: var(--stripe-lilac); }

  .address-band {
    position: absolute; left: 0; right: 0; top: 294px; bottom: 0;
    background: var(--navy-deep);
    display: flex; align-items: center; justify-content: center;
    font-size: 17px; letter-spacing: .6px;
  }

  /* Logo side */
  .card--front { top: 480px; height: 400px; background: var(--white); }
  .front-panel {
    position: absolute; top: 0; bottom: 0; left: 205px; width: 300px;
    background: var(--navy);
    display: flex; flex-direction: column; align-items: center; justify-content: center;
    text-align: center;
  }
  .front-panel .brand-mark { color: var(--silver); font-size: 30px; }
  .front-panel .brand-mark .dot { background: var(--silver); }
  .front-panel .doctor-name { color: var(--silver); font-size: 38px; margin-top: 28px; }
  .front-panel .specialty { color: var(--accent-blue); font-size: 20px; letter-spacing: .6px; }
</style>
</head>
<body>
<main class="canvas">
  <section class="card card--contact">
    <div class="identity">
      <div class="brand-mark"><span class="dot"></span>VARELA</div>
      <h1 class="doctor-name">Dr. Mateo Varela</h1>
      <p class="specialty">Cirugia Plastica</p>
    </div>
    <ul class="contact-list">
      <li>Email : mateo@drvarela.com</li>
      <li>Web : www.drvarela.com</li>
      <li>Tel : 021 (33) 3581 2270</li>
      <li>Cel : 33 3746 0928</li>
    </ul>
    <div class="color-rule"><span></span><span></span><span></span><span></span><span></span><span></span></div>
    <div class="address-band">Av. Robles 1820 Int 45 Torre Medica Central Guadalajara, Jal Mexico</div>
  </section>

  <section class="card card--front">
    <div class="front-panel">
      <div class="brand-mark"><span class="dot"></span>VARELA</div>
      <h2 class="doctor-name">Dr. Mateo Varela</h2>
      <p class="specialty">Cirugia Plastica</p>
    </div>
  </section>
</main>
</body>
</html>
```